Stylish Design With Simple UI For Appointment Site

ONE WEEK TO GO - STILL CONSIDERING NEW DESIGNS!

Note: Logo file now attached. Extra credit to anyone who offers basic HTML templates in the final deliverable, incorporating the individual components of the design (using DIVs and CSS).

There are two key requirements for this site:

1. It makes our site look like one of the most professional of its kind. We want to look the part;
2. It has a very simple, straight-forward user interface. We're nothing without being intuitive.

Our site will be used by other businesses to set up their own online booking systems.

Logo samples attached. The colour scheme is not yet set but two possible options are:

1. Dark (#323B3A) & Blue (#12B5D4) on White background
2. White & Yellow (#FEF102) on Grey (#3A3A3C) background

For inspiration, and an idea of what we like, take a look at quillpost.example - it's very clear and eye-catching, although its pages are longer than we would like ours to be. Oh but we don't need a chimp! Instead of the section with the chimp in, we would like a changing image headline section on the home page, in the style of bellvarine.example.co.uk (with a less high image; we have attached one image which you may want to try out with this, but happy to see other ideas).

Any graphics included must be royalty free and free for commercial use. Fonts should be readily available and specified.

We would like to see the design applied to the following pages:

1. The main public home page (features header, login prompt, menu, changing image banner with headlines, main body, footer menu).
2. A secondary public page (features a similar layout to home page but without image headline banner, includes extra panels/body detail).
3. The Control Panel page (features several list panels and an add appointment button).
4. A list-style administration page (with popup item editor window).
5. A settings administration page (with form).

In that order, a sample walk-through design spec will be attached.

To summarise, we are looking for someone to put forward not only a design but something which also focuses on the user interface. The designer should consider all of the examples and guidance given, but shouldn't let that limit any innovation.

Happy to respond to any questions and give constant feedback.

Thank you.

-*-*-*-*-*-*-*-*-*-*-*-*-*-*-*-*-

Update, 18th Nov 2011:

1. I'm about the upload the logos so you can incorporate these into your designs.

2. A UI question of mine is how to move from a list view (e.g. Resources) to editing one of those items in the list. In the spec document I showed a popup editor for these items but I don't know if that's the best thing to do. Happy to see other ideas on this - whatever the best user experience would be.

3. On the designs in the spec document I've not included any help functionality. It would be good to include pieces of guidance on each page of the administration area to help the user - guess these could either be info panels on the pages themselves or info popups. Again, would be good to see some ideas in the designs.

Also, just to be clear, I am really looking for something that looks like a modern innovative "web app" rather than it looking like a promotional corporate web site.

Target Market(s)

Owners of businesses of all types (e.g. salons, small hotels, surgeries, etc).

Industry/Entity Type

Commercial

Requirements
Must have
• Headline image transition panel on home page.

Layout, graphic and font styles along similar lines to quillpost.example, bellvarine.example.co.uk, etc.
Nice to have
• Blog feed panel on the home page.

Innovative ideas for improvements to the spec.
Should not have
• Anything which can't be practically rendered when the design is converted to HTML.

Should not be overly influenced by the layout and style in the attached spec - that should just be a guide to the content and layout of the site.

```html
<!DOCTYPE html>
<html lang="en">
<head>
<meta charset="utf-8">
<title>Slotwise — Online Booking</title>
<link rel="stylesheet" href="https://fonts.googleapis.com/css2?family=Arimo:wght@400;700&family=PT+Sans:wght@400;700&family=Arvo:wght@700&family=Oswald:wght@500;600&display=swap">
<style>
:root{
  --header-bg:#3a3a3c;
  --tab-bg:#2e2e30;
  --yellow-top:#f0e100;
  --yellow-bottom:#ffcb00;
  --accent-yellow:#ffd200;
  --orange:#ff9000;
  --hero-black:#000;
  --body-bg:#d0d2cf;
  --card-bg:#efefef;
  --text-dark:#222;
  --heading:#3c3c3c;
  --footer-bg:#1d1b18;
  --white:#fff;
}
*{box-sizing:border-box;margin:0;padding:0}
html,body{width:1200px;height:1127px;overflow:hidden}
body{position:relative;font-family:"PT Sans",sans-serif;background:var(--body-bg);color:var(--text-dark)}

.site-header{position:absolute;left:0;top:0;width:1200px;height:176px;background:var(--header-bg);border-bottom:1px solid #f5f5f5}
.brand{position:absolute;left:112px;top:30px;display:flex;flex-direction:column;align-items:flex-start;gap:14px}
.brand-mark{width:44px;height:44px;background:var(--accent-yellow)}
.brand-name{font-family:"PT Sans",sans-serif;font-size:21px;letter-spacing:4px;color:var(--white);font-weight:400}

.login-form{position:absolute;left:794px;top:27px;font-size:11px;color:var(--white)}
.login-row{display:flex;align-items:center;height:27px;margin-bottom:8px}
.login-row label{width:70px}
.login-row .field{width:227px;height:27px;background:var(--white);border:1px solid #111;color:#999;font-size:10px;padding:6px 7px}
.login-actions{display:flex;align-items:center;margin-left:70px;margin-top:2px}
.btn-login{width:87px;height:25px;background:linear-gradient(90deg,#ffd800,#ff9c00);color:#222;font-size:13px;padding:4px 12px;font-family:"PT Sans",sans-serif}
.forgot{margin-left:9px;color:var(--white);text-decoration:underline;font-size:11px}

.main-nav{position:absolute;left:113px;top:138px;display:flex;gap:2px}
.main-nav a{height:38px;padding:10px 20px 0;border:1px solid #222;border-bottom:none;border-radius:10px 10px 0 0;background:var(--tab-bg);color:var(--white);font-size:14px;text-decoration:none;letter-spacing:.3px}
.main-nav a.active{background:var(--accent-yellow);color:#111;border-color:var(--accent-yellow);padding:11px 24px 0}

.promo-band{position:absolute;left:0;top:177px;width:1200px;height:381px;background:linear-gradient(var(--yellow-top),var(--yellow-bottom));border-bottom:1px solid #f5e39a}
.locale{position:absolute;right:108px;top:0;width:200px;height:30px;background:#1e1e1e;color:var(--white);font-size:12.5px;text-align:center;padding-top:5px;clip-path:polygon(0 0,100% 0,93% 100%,7% 100%);border-radius:0 0 10px 10px}

.hero{position:absolute;left:113px;top:42px;width:977px;height:283px;border-radius:10px;overflow:hidden;background:var(--hero-black)}
.hero-photo{position:absolute;left:0;top:0;width:440px;height:283px;background:radial-gradient(ellipse at 30% 55%,#f2f2f2 0%,#c9c9c9 45%,#6e6e6e 75%,#000 100%)}
.hero-title{position:absolute;right:19px;top:23px;background:var(--orange);color:var(--white);font-family:"Arvo",serif;font-size:23px;padding:7px 15px 7px 16px}
.hero-sub{position:absolute;right:19px;top:66px;background:var(--orange);color:var(--white);font-family:"Arvo",serif;font-size:14px;padding:4px 17px 7px 22px}
.hero-next{position:absolute;left:886px;top:116px}
.btn-pill{position:absolute;display:flex;align-items:center;justify-content:center;gap:12px;background:linear-gradient(#3a3a3a,#050505);border-radius:10px;color:var(--accent-yellow);font-family:"Oswald",sans-serif;font-weight:600;font-size:21px;letter-spacing:.5px}
.hero .btn-pill{left:799px;top:221px;width:159px;height:40px}

.content-card{position:absolute;left:113px;top:588px;width:977px;height:393px;background:var(--card-bg);border-radius:10px;box-shadow:0 0 3px rgba(0,0,0,.25)}
.card-col{position:absolute;top:0}
.col-about{left:0;width:480px}
.col-news{left:497px;width:480px}
.card-col h2{font-family:"Arimo",sans-serif;font-weight:400;font-size:24px;color:var(--heading);padding:24px 0 0 33px;height:65px;border-bottom:1px solid #e0e0e0}
.col-news h2{padding-left:33px}
.portrait{margin:16px 0 0 32px;width:416px;height:148px;background:var(--white);padding:4px;box-shadow:0 0 3px rgba(0,0,0,.25)}
.portrait div{width:100%;height:100%;background:linear-gradient(90deg,#5a7fa0 0%,#b88866 25%,#9fb3c0 55%,#d7e2e8 100%)}
.card-col p{font-size:13px;line-height:17px;color:var(--text-dark);padding:0 30px 0 33px}
.col-about p{margin-top:20px}
.news-item{margin-top:10px}
.news-item:first-of-type{margin-top:11px}
.news-item h3{font-size:13px;font-weight:700;padding:0 0 7px 33px}
.news-item+.news-item{margin-top:24px}
.content-card .btn-pill{left:765px;top:324px;width:194px;height:40px;border:1px solid #111}

.site-footer{position:absolute;left:0;top:1018px;width:1200px;height:109px;background:var(--footer-bg);border-top:2px solid #fafafa;color:var(--white);font-size:11px;text-align:center}
.footer-nav{margin-top:34px}
.footer-nav a{color:var(--white);text-decoration:none;padding:0 8px}
.footer-nav a.active{color:var(--accent-yellow)}
.footer-nav span{color:var(--white)}
.copyright{margin-top:3px}
</style>
</head>
<body>

<header class="site-header">
  <div class="brand">
    <div class="brand-mark"></div>
    <span class="brand-name">SLOTWISE</span>
  </div>

  <form class="login-form">
    <div class="login-row"><label>Username</label><div class="field">Username</div></div>
    <div class="login-row"><label>Password</label><div class="field">**************</div></div>
    <div class="login-actions"><div class="btn-login">LOGIN</div><a class="forgot" href="#">Forgotten password?</a></div>
  </form>

  <nav class="main-nav">
    <a class="active" href="#">HOME</a>
    <a href="#">FEATURES</a>
    <a href="#">PRICING</a>
    <a href="#">CONTACT US</a>
  </nav>
</header>

<section class="promo-band">
  <div class="locale">United States- English</div>
  <div class="hero">
    <div class="hero-photo" role="img" aria-label="Close-up photograph of a clock face"></div>
    <div class="hero-title">LOREM IPSUM DOLOR SIT AMET</div>
    <div class="hero-sub">Lorem ipsum dolot sit amet</div>
    <svg class="hero-next" width="46" height="64" viewBox="0 0 46 64" aria-hidden="true">
      <path d="M2 2 L44 32 L4 62 L16 32 Z" fill="#2a2a2a" stroke="#555" stroke-width="1.5"/>
    </svg>
    <a class="btn-pill" href="#">SIGN UP
      <svg width="26" height="26" viewBox="0 0 26 26" aria-hidden="true"><circle cx="13" cy="13" r="11" fill="none" stroke="#ffd200" stroke-width="2.5"/><path d="M7 13h10M13 8l5 5-5 5" fill="none" stroke="#ffd200" stroke-width="2.5"/></svg>
    </a>
  </div>
</section>

<main class="content-card">
  <section class="card-col col-about">
    <h2>Make Yourself Available</h2>
    <div class="portrait"><div role="img" aria-label="Photograph of a smiling businesswoman"></div></div>
    <p>Lorem ipsum dolor sit amet, consectetur adipiscing elit. Ut eget arcu in sapien sollicitudin adipiscing venenatis vitae sem. Morbi massa sem, fringilla sit amet fermentum vitae, dictum a urna. Phasellus id neque eu augue bibendum vulputate. Ut vitae lectus nulla. Ut varius vestibulum quam eget dapibus.</p>
  </section>

  <section class="card-col col-news">
    <h2>What’s Happenning?</h2>
    <article class="news-item">
      <h3>29th Nov, 2011</h3>
      <p>Lorem ipsum dolor sit amet, consectetur adipiscing elit. Ut eget arcu in sapien sollicitudin adipiscing venenatis vitae sem. Morbi massa sem, fringilla sit amet fermentum vitae, dictum a urna. Phasellus id neque eu augue bibendum vulputate.</p>
    </article>
    <article class="news-item">
      <h3>30th Nov, 2011</h3>
      <p>Lorem ipsum dolor sit amet, consectetur adipiscing elit. Ut eget arcu in sapien sollicitudin adipiscing venenatis vitae sem. Morbi massa sem, fringilla sit amet fermentum vitae, dictum a urna. Phasellus id neque eu augue bibendum vulputate.</p>
    </article>
  </section>

  <a class="btn-pill" href="#">MORE NEWS
    <svg width="26" height="26" viewBox="0 0 26 26" aria-hidden="true"><circle cx="13" cy="13" r="11" fill="none" stroke="#ffd200" stroke-width="2.5"/><path d="M7 13h10M13 8l5 5-5 5" fill="none" stroke="#ffd200" stroke-width="2.5"/></svg>
  </a>
</main>

<footer class="site-footer">
  <nav class="footer-nav">
    <a class="active" href="#">Home</a><span>|</span>
    <a href="#">Features</a><span>|</span>
    <a href="#">Pricing</a><span>|</span>
    <a href="#">Contacct Us</a>
  </nav>
  <p class="copyright">© 2011, All Rights Reserved, slotwise.example</p>
</footer>

</body>
</html>
```